New Company Business Card Design

I have a new company logo and I want a new business card design. I dont know if the logo file i attached is in the correct format or quality. We are a New York City Specialty construction Firm specializing in high risk out of the box projects. I want a simple and classy business card that people will his card is as crisp as the work his company does.

Target Market(s)

Clients in the heavy construction industry in New York City

Industry/Entity Type

Construction Company

Contact Information for Business Card

Simple Classy - DIFFERENT

Font styles to use
Other font styles liked:
• Mach the logo font in some way

Colors

Designer to choose colors to be used in the design.

Requirements
Must have
• Uniqueness
Nice to have
• Nothing particular - Just different and classy - Timeless
Should not have
• Goofy Shit or Gimmicky shit

```html
<!DOCTYPE html>
<html lang="en">
<head>
<meta charset="utf-8">
<title>Kestrel Builders – Business Cards</title>
<link href="https://fonts.googleapis.com/css2?family=Montserrat:wght@800&family=Roboto:wght@400;500;700&display=swap" rel="stylesheet">
<style>
  :root {
    --brand-blue: #0a66b0;
    --ink: #111111;
    --paper: #ffffff;
    --backdrop: #2b2b2b;
  }
  html, body {
    margin: 0;
    width: 1200px;
    height: 900px;
    overflow: hidden;
    background: var(--backdrop);
    font-family: "Roboto", Arial, sans-serif;
  }
  .card {
    position: absolute;
    width: 600px;
    height: 340px;
    overflow: hidden;
    box-shadow: 0 18px 40px rgba(0,0,0,.55);
  }
  /* Front */
  .card--front {
    left: 70px;
    top: 80px;
    background: var(--brand-blue);
  }
  .brand-lockup {
    position: absolute;
    left: 0; right: 0;
    top: 118px;
    display: flex;
    align-items: center;
    justify-content: center;
    gap: 14px;
  }
  .brand-mark {
    width: 26px;
    height: 26px;
    background: var(--ink);
  }
  .brand-name {
    font-family: "Montserrat", Arial, sans-serif;
    font-weight: 800;
    font-size: 38px;
    letter-spacing: 1px;
    color: var(--paper);
    line-height: 1;
  }
  .brand-name small {
    display: block;
    font-size: 15px;
    letter-spacing: 7px;
    margin-top: 8px;
  }
  .front-web {
    position: absolute;
    left: 0; right: 0;
    top: 262px;
    text-align: center;
    color: var(--paper);
    font-size: 15px;
  }
  /* Back */
  .card--back {
    left: 530px;
    top: 480px;
    background: var(--paper);
  }
  .card--back svg.wave { position: absolute; inset: 0; }
  .back-brand {
    position: absolute;
    left: 46px;
    top: 100px;
    display: flex;
    align-items: center;
    gap: 10px;
  }
  .back-brand .brand-name { color: var(--brand-blue); font-size: 30px; }
  .back-brand .brand-name small { font-size: 12px; letter-spacing: 5px; }
  .holder {
    position: absolute;
    right: 44px;
    top: 24px;
    text-align: right;
  }
  .holder-name {
    color: var(--brand-blue);
    font-weight: 500;
    font-size: 20px;
    line-height: 1;
  }
  .holder-role {
    color: var(--ink);
    font-weight: 700;
    font-size: 10px;
    margin-top: 3px;
  }
  .holder-rule {
    width: 120px;
    height: 2px;
    background: var(--brand-blue);
    margin: 8px 0 0 auto;
  }
  .contact-list {
    position: absolute;
    right: 24px;
    top: 158px;
    list-style: none;
    margin: 0; padding: 0;
    color: var(--paper);
    font-size: 13.5px;
  }
  .contact-list li {
    display: flex;
    justify-content: flex-end;
    align-items: center;
    gap: 8px;
    height: 24px;
  }
  .contact-icon {
    width: 17px; height: 17px;
    display: block;
  }
  .address {
    position: absolute;
    left: 130px;
    bottom: 20px;
    color: var(--paper);
    font-size: 15px;
    line-height: 1.3;
  }
</style>
</head>
<body>

<section class="card card--front">
  <div class="brand-lockup">
    <span class="brand-mark"></span>
    <div class="brand-name">KESTREL<small>BUILDERS, INC.</small></div>
  </div>
  <div class="front-web">www.kestrelbuild.com</div>
</section>

<section class="card card--back">
  <svg class="wave" viewBox="0 0 600 340" width="600" height="340" aria-hidden="true">
    <path d="M0,230 C120,250 230,240 320,172 S500,92 600,86 L600,340 L0,340 Z" fill="#0a66b0"/>
    <path d="M0,225 C120,245 230,235 318,167 S500,87 600,81" fill="none" stroke="#111" stroke-width="3"/>
    <path d="M330,178 C400,128 480,104 600,98" fill="none" stroke="#111" stroke-width="2"/>
    <path d="M30,262 C130,262 215,246 290,206" fill="none" stroke="#fff" stroke-width="5"/>
    <path d="M30,254 C130,254 212,238 286,199" fill="none" stroke="#111" stroke-width="2"/>
  </svg>

  <div class="back-brand">
    <span class="brand-mark"></span>
    <div class="brand-name">KESTREL<small>BUILDERS, INC.</small></div>
  </div>

  <div class="holder">
    <div class="holder-name">ROWAN PELL</div>
    <div class="holder-role">OWNER</div>
    <div class="holder-rule"></div>
  </div>

  <ul class="contact-list">
    <li>555-010-2040
      <svg class="contact-icon" viewBox="0 0 16 16"><rect width="16" height="16" fill="#fff"/><path d="M4 3l2 0 1 3-1.5 1a6 6 0 0 0 3.5 3.5l1-1.5 3 1v2c0 .6-.5 1-1 1A10 10 0 0 1 3 4c0-.5.4-1 1-1z" fill="#0a66b0"/></svg>
    </li>
    <li>555-010-2041
      <svg class="contact-icon" viewBox="0 0 16 16"><rect width="16" height="16" fill="#fff"/><rect x="3" y="6" width="10" height="7" fill="#0a66b0"/><rect x="5" y="3" width="6" height="3" fill="#0a66b0"/></svg>
    </li>
    <li>hello@kestrelbuild.com
      <svg class="contact-icon" viewBox="0 0 16 16"><rect width="16" height="16" fill="#fff"/><rect x="3" y="4.5" width="10" height="7" fill="none" stroke="#0a66b0" stroke-width="1.5"/><path d="M3 4.5l5 4 5-4" fill="none" stroke="#0a66b0" stroke-width="1.5"/></svg>
    </li>
    <li>www.kestrelbuild.com
      <svg class="contact-icon" viewBox="0 0 16 16"><rect width="16" height="16" fill="#fff"/><circle cx="8" cy="8" r="5" fill="none" stroke="#0a66b0" stroke-width="1.5"/><path d="M3 8h10M8 3c-2.5 3-2.5 7 0 10M8 3c2.5 3 2.5 7 0 10" fill="none" stroke="#0a66b0" stroke-width="1"/></svg>
    </li>
  </ul>

  <div class="address">Level 2 Harbor Court<br>Pier Road, Northport</div>
</section>

</body>
</html>
```